Need help in designing new business card utilizing our new logo.

BuildMarq Solutions works with Construction Business Owners, Managers & IT Professionals to strengthen software usage and increase user productivity.

Our Construction Accounting and Mobile Field Management Software Clients engage with us in the following areas:

New Software Implementations
Software Re-Implementations
Redesigning Software Usage at the User Level
Project Coordination & Management
Continued Software Support

Old tag line:
Weighing Options - Implementing Solutions

www.buildmarq-solutions.example

Stride 4 is a product, but not needed for a new business card.

```html
<!DOCTYPE html>
<html lang="en">
<head>
<meta charset="utf-8">
<title>BuildMarq Solutions – Business Card</title>
<link href="https://fonts.googleapis.com/css2?family=Roboto:ital,wght@0,300;0,400;0,700;1,400;1,700&family=Roboto+Condensed:wght@400;700&display=swap" rel="stylesheet">
<style>
  :root {
    --brand-blue: #1a1fb8;
    --brand-grey: #c9cacc;
    --text-grey: #6f7073;
    --light-text: #ffffff;
    --card-white: #fbfbfb;
    --page-bg: #e9e7e3;
  }
  * { margin: 0; padding: 0; box-sizing: border-box; }
  html, body { width: 1200px; height: 911px; overflow: hidden; }
  body {
    background: var(--page-bg);
    font-family: "Roboto", Arial, sans-serif;
    position: relative;
  }
  .card {
    position: absolute;
    width: 560px;
    height: 320px;
    background: var(--card-white);
    box-shadow: 0 6px 18px rgba(0,0,0,0.18);
    overflow: hidden;
  }
  /* Front */
  .card-front { left: 50px; top: 110px; }
  .front-brand {
    position: absolute; left: 48px; top: 46px;
    display: flex; align-items: center; gap: 16px;
  }
  .brand-square { width: 40px; height: 40px; background: var(--brand-blue); }
  .brand-name {
    font-family: "Roboto Condensed", Arial, sans-serif;
    font-weight: 700; font-size: 38px; color: var(--brand-blue);
    letter-spacing: 0.5px;
  }
  .band { position: absolute; top: 138px; height: 130px; }
  .band-name { left: 0; width: 300px; background: var(--brand-blue); color: var(--light-text); padding: 26px 0 0 34px; }
  .band-contact { left: 300px; width: 260px; background: var(--brand-grey); color: var(--light-text); padding: 22px 20px 0 0; text-align: right; }
  .person-name { font-family: "Roboto Condensed", Arial, sans-serif; font-weight: 700; font-size: 21px; text-transform: uppercase; }
  .person-role { font-size: 13px; text-transform: uppercase; margin-top: 4px; }
  .person-address { font-size: 13px; line-height: 1.35; margin-top: 4px; }
  .contact-line { display: flex; justify-content: flex-end; align-items: center; gap: 8px; font-size: 12px; font-weight: 300; line-height: 22px; }
  .contact-line svg { width: 11px; height: 11px; fill: var(--light-text); }
  .front-tagline {
    position: absolute; right: 26px; bottom: 16px;
    font-size: 13px; letter-spacing: 0.6px; color: var(--text-grey); text-transform: uppercase;
  }
  /* Back */
  .card-back { left: 600px; top: 470px; }
  .back-brand {
    position: absolute; right: 40px; top: 36px;
    display: flex; align-items: center; gap: 12px;
  }
  .back-brand .brand-square { width: 30px; height: 30px; }
  .back-brand .brand-name { font-size: 26px; }
  .back-copy { position: absolute; left: 30px; top: 128px; right: 24px; }
  .back-heading { font-weight: 700; font-style: italic; font-size: 14px; color: var(--brand-blue); text-transform: uppercase; line-height: 1.3; }
  .service-list { font-style: italic; font-size: 13px; color: var(--text-grey); line-height: 1.5; margin-top: 8px; }
  .old-tagline { font-weight: 700; font-style: italic; font-size: 13px; color: var(--brand-blue); text-transform: uppercase; margin-top: 10px; }
</style>
</head>
<body>
  <section class="card card-front" aria-label="Business card front">
    <div class="front-brand">
      <span class="brand-square"></span>
      <span class="brand-name">BUILDMARQ SOLUTIONS</span>
    </div>
    <div class="band band-name">
      <p class="person-name">Dana R. Whitfield</p>
      <p class="person-role">Owner</p>
      <p class="person-address">14b harbor street-PMB118<br>millbrook NY 12545</p>
    </div>
    <div class="band band-contact">
      <p class="contact-line">555-010-4420 ext.100
        <svg viewBox="0 0 24 24"><path d="M6.6 10.8a15 15 0 0 0 6.6 6.6l2.2-2.2c.3-.3.7-.4 1-.2 1.1.4 2.3.6 3.6.6.6 0 1 .4 1 1V20c0 .6-.4 1-1 1A17 17 0 0 1 3 4c0-.6.4-1 1-1h3.5c.6 0 1 .4 1 1 0 1.3.2 2.5.6 3.6.1.3 0 .7-.2 1z"/></svg></p>
      <p class="contact-line">555-010-7781
        <svg viewBox="0 0 24 24"><path d="M7 1h10a2 2 0 0 1 2 2v18a2 2 0 0 1-2 2H7a2 2 0 0 1-2-2V3a2 2 0 0 1 2-2zm0 3v14h10V4z"/></svg></p>
      <p class="contact-line">dana.whitfield@buildmarq-solutions.example
        <svg viewBox="0 0 24 24"><path d="M2 5h20v14H2zm2 2v.5l8 5 8-5V7z"/></svg></p>
      <p class="contact-line">www.buildmarq-solutions.example
        <svg viewBox="0 0 24 24"><circle cx="12" cy="12" r="10"/></svg></p>
    </div>
    <p class="front-tagline">Construction Accounting Software Consultants</p>
  </section>

  <section class="card card-back" aria-label="Business card back">
    <div class="back-brand">
      <span class="brand-square"></span>
      <span class="brand-name">BUILDMARQ</span>
    </div>
    <div class="back-copy">
      <p class="back-heading">Our construction accounting and mobile field management<br>software clients engage with us in the following areas:</p>
      <p class="service-list">New Software Implementations • Software Re-Implementations<br>Redesigning Software Usage at the User Level<br>Project Coordination &amp; Management • Continued Software Support</p>
      <p class="old-tagline">Weighing Options - Implementing Solutions</p>
    </div>
  </section>
</body>
</html>
```